Web Design Project for a Software & Consulting Company

We have just completed a recent ArtHive project for a new logo (see attached).
As the next stage of our rebranding we now require a website re-design to complement the new logo.
Our current site, http://www.corvanisoft.com was built in-house and does not come across as professional as we would like. We supply software and associated services to some of the world’s largest oil companies and we need our site to reflect that level of client.
We will also be posting another design project for brochures, PowerPoint slides and other materials very soon.
We would like designs for…
Home page
Product page
• JTP
• LBV
• SGF
Services
News page
About Us page
Contact Us page
Page for mobile devices that gives basic company and product information
Currently the site is small but we intend to increase content to include white papers etc. this should be taken into account when designing the navigation therefore we would prefer navigation through styled text links rather than images.
Colour schemes should broadly be taken from our new logo, where the dark blue and dark green from the left and right sides of the logo are the main colours, but other, brighter accent colours can be used to highlight sections or content.
Dark Blue = C:88, M:55, Y:44, K:28
Dark Green = C:87, M:53, Y:50, K:50
NB: Don’t use the logo on our current site, make sure you use the one attached.
We would prefer the final file format to be a layered PSD.
The site should be clean and professional and communicate the following...
• That we have a great depth and breadth of knowledge about our customers’ business, enabling us to deliver the best systems and solutions.
• That we are a leading provider of cost estimation and control solutions to the oil and gas industry.
• The benefits of our software and consulting services.
• Show that we deliver outstanding customer service and value with a very high level of professionalism
• The site should have no Flash and be able to self-adjust to fit any screen size.
Things to avoid …
• Obvious and clichéd oil industry imagery, no oil rigs
• Cartoon style graphics
Our Background
We are an integrated software and consulting organization specialising in the drilling side of the oil and gas industry. Simply put our software helps companies better understand, predict and communicate the cost of drilling wells.
We have 3 software products and a consulting offering consisting of…
• JTP - Probabilistic time and cost software
• LBV – Cost tracking and reporting software
• SGF – (currently known as TrailMemo) – Lessons learned software
• Consulting services
Our systems are in use in over 30 countries with a broad range of clients including: QZ, Dunmara, Pilk, Ravenor, FELO Curvasti, VASTIRO and Quarlix.
Our current site can be found at www.corvanisoft.com
Our main competitors are
• http://www.lumbrok.com/
• http://www.vantiquo.com/
• http://www.ktv.com/services/software-solutions/z4-
Our depth of drilling knowledge, quality of software and collaboration with clients differentiate us form the competition.
We strive for very high levels of customer service.
We look forward to receiving your designs!
Updates
Thanks to all the designers who have submitted a design, we appreciate the effort.
We will do our best to give individual feedback on each design but given that many are quite similar we thought we would give some general feedback first.
Nearly all the designs submitted so far have been slight variations on…
-
Top Menu
-
Scrolling Photo Banner
-
4 Columns
-
Body
-
Deep Footer
These designs are well executed but they are basically the same layout as our existing site and while there is nothing inherently wrong with this layout we would like to see some designs that are a bit more innovative and different. We don’t really want just a polished version of our current site.
Thanks again,
CVS
Thanks to everyone who has submitted a design, the response has been great.
We are close to making a decision so if you are intending to submit a design please do it soon, the deadline is only a few days away.
Thanks again.
CVS
Target Market(s)
Mid to high level executives
Industry/Entity Type
Oil And Gas
Look and feel

```html
<!DOCTYPE html>
<html lang="en">
<head>
<meta charset="utf-8">
<title>Corvani Technologies</title>
<link href="https://fonts.googleapis.com/css2?family=Ubuntu:wght@300;400;500;700&display=swap" rel="stylesheet">
<style>
:root{
  --teal:#1fb3b1;
  --teal-dark:#139c9a;
  --ink:#233a44;
  --ink-dark:#1e2e33;
  --grey-text:#9a9a9a;
  --hero-a:#7aa2ab;
  --hero-b:#5f8994;
  --bar:#3a3a3a;
  --footer:#414141;
  --footer-text:#e6e6e6;
  --band:#f3f3f3;
  --rule:#e4e4e4;
  --red:#c91818;
}
*{box-sizing:border-box;margin:0;padding:0}
html,body{width:1023px;height:1200px;overflow:hidden}
body{position:relative;background:#fff;font-family:"Ubuntu",sans-serif;color:#555}
.abs{position:absolute}

.top-bar{left:0;top:0;width:1023px;height:7px;background:var(--bar)}
.call-tab{left:749px;top:0;width:127px;height:25px;background:var(--bar);border-radius:0 0 14px 14px;color:#fff;font-size:10px;line-height:25px;text-align:center}

.brand{left:111px;top:40px;display:flex;align-items:center;gap:8px}
.brand-dot{width:34px;height:34px;border-radius:50%;background:var(--ink)}
.brand-name{font-size:20px;font-weight:500;color:var(--ink);letter-spacing:.5px;line-height:1}
.brand-name small{display:block;font-size:9px;letter-spacing:3px;margin-top:3px}

.main-nav a{position:absolute;top:59px;height:24px;line-height:24px;font-size:11px;color:var(--ink-dark);text-decoration:none;letter-spacing:.3px}
.main-nav a.active{background:var(--teal);color:#fff;width:60px;text-align:center;border-radius:2px;font-weight:500}

.hero{left:0;top:124px;width:1023px;height:316px;background:linear-gradient(135deg,var(--hero-a),var(--hero-b))}
.hero-title{left:110px;top:164px;width:390px;color:#fff;font-weight:300;font-size:21px;line-height:33px;white-space:nowrap}
.hero-title b{font-weight:400;font-size:27px;color:#13262c}
.hero-copy{left:110px;top:266px;width:370px;color:#fff;font-size:11.5px;line-height:19.5px;font-weight:300}
.btn{position:absolute;height:24px;line-height:24px;text-align:center;font-size:11px;border-radius:3px;text-decoration:none}
.btn-light{background:linear-gradient(#fff,#e6e6e6);border:1px solid #cfcfcf;color:#444}
.btn-teal{background:linear-gradient(var(--teal),var(--teal-dark));color:#fff}
.hero-frame{left:493px;top:150px;width:419px;height:232px;border:4px solid #e9eef0;border-radius:3px;box-shadow:0 4px 10px rgba(0,0,0,.3);background:linear-gradient(160deg,#c9e3f2,#5b8fb5 55%,#1d2c3a)}

.feature{position:absolute;top:402px;width:192px;height:206px;background:#fff;border-top:3px solid var(--ink);box-shadow:0 3px 12px rgba(0,0,0,.16);padding:16px 15px}
.feature.lead{border-top-color:var(--teal)}
.feature h3{font-size:12.5px;font-weight:400;color:var(--ink-dark);margin-bottom:10px;white-space:nowrap}
.feature p{font-size:10.5px;line-height:17px;color:var(--grey-text);font-weight:300;height:112px}
.feature .btn{position:relative;display:block;width:162px;height:23px;line-height:23px}

.welcome-photo{left:111px;top:640px;width:220px;height:147px;border:4px solid #fff;box-shadow:0 1px 5px rgba(0,0,0,.25);background:linear-gradient(135deg,#e9ecee,#c8d0d5 50%,#d9c07d)}
.welcome-title{left:362px;top:638px;font-size:21px;font-weight:400;color:var(--ink-dark);letter-spacing:-.5px}
.welcome-copy{left:362px;top:674px;width:550px;font-size:11px;line-height:18px;color:var(--grey-text);font-weight:300}

.clients{left:0;top:820px;width:1023px;height:71px;background:var(--band);border-top:1px solid var(--rule)}
.client{position:absolute;top:24px;transform:translateX(-50%);font-size:14px;font-weight:500;color:#5d6b72;display:flex;align-items:center;gap:5px;white-space:nowrap}
.client i{display:block;width:10px;height:10px;background:#5d6b72}

.footer{left:0;top:891px;width:1023px;height:268px;background:var(--footer);color:var(--footer-text)}
.fcol{position:absolute;top:40px}
.fcol h4{font-size:16px;font-weight:400;margin-bottom:12px}
.fcol p{font-size:9.5px;line-height:14px;margin-bottom:5px}
.fcol li{list-style:none;font-size:9.5px;line-height:19.6px}
.field{width:158px;height:23px;border-radius:3px;background:linear-gradient(#fff,#e8e8e8);font-size:9px;color:#aaa;padding-left:8px;line-height:23px;margin-bottom:9px}
.forgot{font-size:9px;margin:-6px 0 0 5px}
.login{margin-top:9px;width:66px;height:20px;background:linear-gradient(#e02020,var(--red));border-radius:3px;color:#fff;font-size:12px;font-weight:500;line-height:20px;text-align:center}
.author{color:var(--teal)}

.bottom-bar{left:0;top:1159px;width:1023px;height:41px;background:var(--bar);color:#ddd;font-size:10px;line-height:41px;border-top:1px solid #4a4a4a}
.bottom-bar span{position:absolute;left:111px}
.bottom-bar a{position:absolute;color:#ddd;text-decoration:none}
</style>
</head>
<body>
<div class="abs top-bar"></div>
<div class="abs call-tab">Call 1-800-555-0142</div>

<div class="abs brand">
  <div class="brand-dot"></div>
  <div class="brand-name">CORVANI<small>TECHNOLOGIES</small></div>
</div>

<nav class="main-nav">
  <a class="active" style="left:478px" href="#">HOME</a>
  <a style="left:552px" href="#">PRODUCT</a>
  <a style="left:628px" href="#">SERVICES</a>
  <a style="left:705px" href="#">NEWS</a>
  <a style="left:764px" href="#">ABOUT US</a>
  <a style="left:844px" href="#">CONTACT US</a>
</nav>

<section class="abs hero"></section>
<h1 class="abs hero-title"><b>CORVANI</b> have the <b>TOOLS</b> to<br>help companies <b>BETTER</b> manmanage<br>the business of <b>DRILLING</b> wells</h1>
<p class="abs hero-copy">Lorem ipsum dolor sit amet, consectetuer adipiscing elit, sed diam nonummy nibh euismod tincidunt ut laoreet dolore magna aliquam erat volutpat. Ut wisi enim ad minim veniam, quis nostrud exerci tation ullamcorper suscipit lobortis nisl ut aliquip ex ea commodo consequat. Duis autem vel eum.</p>
<a class="btn btn-light" style="left:110px;top:368px;width:97px" href="#">READ MORE</a>
<div class="abs hero-frame" role="img" aria-label="Photo of a businessman behind rising oil barrels and a growth chart"></div>

<div class="feature lead" style="left:111px">
  <h3>TIME &amp; COST ESTIMATION</h3>
  <p>JTP delivers a standardized, systematic approach to undestanding, quantifying and communicating the impact of project risk to all stakeholders.</p>
  <a class="btn btn-teal" href="#">READ MORE</a>
</div>
<div class="feature" style="left:314px">
  <h3>MATERIAL &amp; COST CONTROL</h3>
  <p>Since 1992 LBV has been helping companies optimize their materials and logistics processes and accurately track costs on a daily basis.</p>
  <a class="btn btn-light" href="#">READ MORE</a>
</div>
<div class="feature" style="left:517px">
  <h3>LESSON LEARNED</h3>
  <p>TrailMemo is an advanced lessons learned and knowledge management system for use in the Oil &amp; Gas industry. It's fully searchable and easy to use.</p>
  <a class="btn btn-light" href="#">READ MORE</a>
</div>
<div class="feature" style="left:720px">
  <h3>SERVICES &amp; CONSULTING</h3>
  <p>Software solutions rely on people and processes to deliver results. From analysis through execution we support our clients to improve performance. Read More</p>
  <a class="btn btn-light" href="#">READ MORE</a>
</div>

<div class="abs welcome-photo" role="img" aria-label="Photo of a radiator thermostat, banknotes, coins and a calculator"></div>
<h2 class="abs welcome-title">WELCOME TO CORVANI</h2>
<p class="abs welcome-copy">Lorem ipsum dolor sit amet, consectetuer adipiscing elit, sed diam nonummy nibh euis mod tincidunt ut laoreet dolore magna aliquam erat volutpat. Ut wisi enim ad minim veniam, quis nostrud exerci tation ullamcorper suscipit lobortis nisl ut aliquip ex ea commodo consequat. Duis autem vel eum iriure dolor in hendrerit in vulputate velit esse molestie consequat, vel illum dolore eu feugiat nulla facilisis.</p>
<a class="btn btn-teal" style="left:362px;top:762px;width:96px;height:23px;line-height:23px" href="#">READ MORE</a>

<section class="abs clients">
  <div class="client" style="left:149px">Pilk</div>
  <div class="client" style="left:229px">Dunmara</div>
  <div class="client" style="left:325px">Torvalla</div>
  <div class="client" style="left:415px"><i></i>QZ</div>
  <div class="client" style="left:499px">VASTIRO</div>
  <div class="client" style="left:593px">Brendle</div>
  <div class="client" style="left:692px">Ostrova</div>
  <div class="client" style="left:789px">Ravenor</div>
  <div class="client" style="left:890px">FELO</div>
</section>

<footer class="abs footer">
  <div class="fcol" style="left:130px">
    <h4>Member Login</h4>
    <div class="field">username</div>
    <div class="field">password</div>
    <p class="forgot">Forgot your password</p>
    <div class="login">Log in</div>
  </div>
  <div class="fcol" style="left:326px;width:200px">
    <h4>Testimonials</h4>
    <p>Lorem Ipsum est simplement du faux texte employé.</p>
    <p style="margin-top:10px">If you want us to design your colour chart contact us</p>
    <p class="author" style="margin-top:10px">Mara Jelski</p>
  </div>
  <div class="fcol" style="left:558px">
    <h4>SiteMap</h4>
    <ul style="margin-top:-3px">
      <li>Lorem ipsum dolosdr</li>
      <li>Consectetuer adipisc</li>
      <li>Diam nonummy nibh</li>
      <li>Cincidunt ut laoreget</li>
      <li>Dolore magna aliqua</li>
    </ul>
  </div>
  <div class="fcol" style="left:738px;width:180px">
    <h4>Contact Details</h4>
    <p>Contact details will be appear here contact details here</p>
    <p style="margin-top:12px">Phone No. : 1-800-555-0187</p>
    <p style="margin-top:14px">E-mail : info@corvanisoft.com</p>
  </div>
</footer>

<div class="abs bottom-bar">
  <span>Copyright 2012. CORVANI, All Rights Reserved.</span>
  <a style="left:619px" href="#">Home</a>
  <a style="left:661px" href="#">Product</a>
  <a style="left:712px" href="#">Services</a>
  <a style="left:764px" href="#">News</a>
  <a style="left:804px" href="#">About Us</a>
  <a style="left:861px" href="#">Contact Us</a>
</div>
</body>
</html>
```